Harbourlight Dental Centre Kelvale business cards and presentation folder

dental practice needing innovative black business cards for 2 different dentists witrh appointment details written at the back of the card for the patient.
name of dentists: Dr Anjali R Venkatesan B.D.S., M.P.H (Melb)
Dr. Raj Kalpat B.D.S.

Target Market(s)

professioinal, working class

Industry/Entity Type

Dental Clinic

Contact Information for Business Card

Dr. Raj Kalpat B.D.S.

Font styles to use
Sans Serif

Requirements
Must have
• Front side: logo
• dentist name
• phone number: 07- 5918 2243
• back side: appointment details: date, time,
• Address: 117C, 58 Tarrow Street, Kelvale - 4561, Queensland
• Email: admin@harbourlightdentalkelvale.example.au
• Website: www.harbourlightdental.example.au
• preferable logo colors
Nice to have
• classy look more pleasing

```html
<!DOCTYPE html>
<html lang="en">
<head>
<meta charset="utf-8">
<title>Harbourlight Dental Centre – Business Card</title>
<link rel="stylesheet" href="https://fonts.googleapis.com/css2?family=Tinos:wght@400;700&family=Source+Sans+3:wght@400;600&display=swap">
<style>
  :root {
    --backdrop: #3b2419;
    --card: #0a0b0b;
    --sage: #a9c68a;
    --sage-deep: #98b878;
    --silver: #b6b9bc;
    --ink-soft: #c9cbcc;
    --ink-dark: #141414;
  }
  * { margin: 0; padding: 0; box-sizing: border-box; }
  html, body { width: 1200px; height: 1000px; overflow: hidden; }
  body { background: var(--backdrop); position: relative; font-family: "Source Sans 3", Arial, sans-serif; }

  .card { position: absolute; background: var(--card); box-shadow: 0 6px 18px rgba(0,0,0,.45); }

  /* Front */
  .card-front { left: 170px; top: 240px; width: 570px; height: 320px; }
  .brand-name {
    position: absolute; left: 52px; top: 138px; width: 220px;
    font-family: "Tinos", "Times New Roman", serif; font-weight: 400;
    font-size: 20px; line-height: 1.15; letter-spacing: .5px;
    color: var(--sage); text-transform: uppercase;
  }
  .front-divider { position: absolute; left: 287px; top: 105px; width: 1px; height: 110px; background: var(--silver); opacity: .7; }
  .dentist { position: absolute; left: 310px; top: 104px; }
  .dentist-name {
    font-family: "Tinos", "Times New Roman", serif; font-weight: 700;
    font-size: 20px; color: var(--sage); margin-bottom: 6px;
  }
  .dentist-detail { font-size: 15px; color: var(--ink-soft); line-height: 1.35; }

  /* Back */
  .card-back { left: 495px; top: 495px; width: 525px; height: 300px; overflow: hidden; }
  .appointment-band {
    position: absolute; left: 85px; top: 123px; right: 0; height: 58px;
    background: var(--sage); border-radius: 8px 0 0 8px;
    font-family: "Tinos", "Times New Roman", serif; font-weight: 700; color: var(--ink-dark);
  }
  .appointment-title { position: absolute; left: 18px; top: 8px; font-size: 18px; letter-spacing: .3px; }
  .appointment-field { position: absolute; left: 205px; font-size: 15px; display: flex; align-items: flex-end; }
  .appointment-field.date { top: 10px; }
  .appointment-field.time { top: 31px; }
  .appointment-field span { width: 50px; }
  .appointment-field i { display: block; width: 150px; border-bottom: 1.5px solid var(--ink-dark); margin-bottom: 3px; }

  .contact-list { position: absolute; left: 188px; top: 199px; list-style: none; }
  .contact-list li { display: flex; align-items: center; height: 22px; font-size: 12.5px; color: var(--ink-soft); }
  .contact-list li:nth-child(1) { margin-left: 24px; }
  .contact-list li:nth-child(2) { margin-left: 12px; }
  .contact-icon { width: 15px; height: 15px; margin-right: 8px; flex: none; }
</style>
</head>
<body>

<section class="card card-front" aria-label="Business card front">
  <div class="brand-name">Harbourlight Dental Centre</div>
  <div class="front-divider"></div>
  <div class="dentist">
    <p class="dentist-name">Dr Anjali R Venkatesan</p>
    <p class="dentist-detail">B.D.S., M.P.H (Melb)</p>
    <p class="dentist-detail">07- 5918 2243</p>
  </div>
</section>

<section class="card card-back" aria-label="Business card back">
  <div class="appointment-band">
    <div class="appointment-title">APPOINTEMENT &nbsp;|</div>
    <div class="appointment-field date"><span>DATE</span><i></i></div>
    <div class="appointment-field time"><span>TIME</span><i></i></div>
  </div>

  <ul class="contact-list">
    <li>
      <svg class="contact-icon" viewBox="0 0 16 16" aria-hidden="true">
        <circle cx="8" cy="8" r="8" fill="var(--sage)"/>
        <rect x="4" y="5" width="8" height="6" rx="1" fill="var(--card)"/>
        <path d="M4.3 5.4 8 8.3l3.7-2.9" stroke="var(--sage)" stroke-width="0.9" fill="none"/>
      </svg>
      admin@harbourlightdentalkelvale.example.au
    </li>
    <li>
      <svg class="contact-icon" viewBox="0 0 16 16" aria-hidden="true">
        <circle cx="8" cy="8" r="8" fill="var(--sage)"/>
        <circle cx="8" cy="8" r="4.2" fill="none" stroke="var(--card)" stroke-width="1"/>
        <ellipse cx="8" cy="8" rx="1.8" ry="4.2" fill="none" stroke="var(--card)" stroke-width="0.9"/>
        <path d="M3.8 8h8.4" stroke="var(--card)" stroke-width="0.9"/>
      </svg>
      www.harbourlightdentalkelvale.example.au
    </li>
    <li>
      <svg class="contact-icon" viewBox="0 0 16 16" aria-hidden="true">
        <circle cx="8" cy="8" r="8" fill="var(--sage)"/>
        <path d="M8 12.5s-3-3.3-3-5.5a3 3 0 0 1 6 0c0 2.2-3 5.5-3 5.5z" fill="var(--card)"/>
        <circle cx="8" cy="7" r="1.1" fill="var(--sage)"/>
      </svg>
      117C, 58 Tarrow Street, Kelvale - 4561, Queensland
    </li>
  </ul>
</section>

</body>
</html>
```